Equine Horse Employment site

We need to redesign the layout of Stablemark Hire.co.uk

It will offer Job seekers and Employers the place to look for a job, and look for a candidate.

The logical format needs to be improved and the layout must look highly visually appealing.

It needs to be incredibly simple to use and one click access to any part of the site.

The homepage must convey the following

- Log in and register areas
- Current Job Listings
- Current CV's
- Exclusive Service Club button
- Search box to allow simple searching for Jobs or CVs

We need PSD layouts for Homepage, Job listing Page, CV listing Page, Job Profile and CV Profile. This job is for the design of 5 PSD screens.

Generic page for ancillary page such as about, contact and news.

The biggest competitor is PaddockPost.com

Please ask us any questions and please be prepared to make changes, as we are very particular.

More work will be provided to the winning designer.

thanks

• It must not look cheap or like a job board, it has to have character and feel friendly, and inviting. Please do not submit poor designs that look like a job board, as they will be rejected instantly.

thanks

```html
<!DOCTYPE html>
<html lang="en">
<head>
<meta charset="utf-8">
<title>Contact Us – Stablemark Hire</title>
<link href="https://fonts.googleapis.com/css2?family=Arimo:wght@400;700&display=swap" rel="stylesheet">
<style>
:root{
  --charcoal:#3f3b3c;
  --footer:#433f40;
  --nav-top:#4a4647;
  --nav-bottom:#262324;
  --red:#d9533a;
  --blue:#6fb3dd;
  --blue-dark:#4f97c7;
  --ink:#3a3a3a;
  --muted:#8a8a8a;
  --line:#c9c9c9;
  --link:#8fc3e6;
  --map-sand:#eae2cf;
  --map-warm:#f1d49a;
  --map-river:#c9d4de;
  --white:#ffffff;
}
*{box-sizing:border-box;margin:0;padding:0}
html,body{width:1200px;height:832px;overflow:hidden;background:var(--white);font-family:"Arimo",Arial,sans-serif;color:var(--ink)}
.page{position:relative;width:1200px;height:832px}
a{text-decoration:none;color:inherit}

/* top bar */
.topbar{position:absolute;left:0;top:0;width:1200px;height:33px;background:var(--charcoal)}
.tab{position:absolute;top:4px;height:29px;font-size:14.5px;font-weight:700;display:flex;align-items:center;justify-content:center;border-radius:3px 3px 0 0}
.tab--seekers{left:196px;width:112px;background:var(--white);color:#6a6a6a}
.tab--employers{left:313px;width:105px;background:var(--red);color:var(--white);height:28px;border-radius:3px}
.topbar__prompt{position:absolute;left:733px;top:9px;color:var(--white);font-size:14px;font-weight:700}
.btn-post{position:absolute;left:899px;top:4px;width:96px;height:25px;background:var(--red);color:var(--white);font-size:15px;font-weight:700;display:flex;align-items:center;justify-content:center;border-radius:3px}

/* header */
.brand{position:absolute;left:202px;top:92px;display:flex;align-items:center;gap:10px}
.brand__mark{width:20px;height:20px;background:var(--red);border-radius:50%}
.brand__name{font-size:22px;font-weight:400;color:#2b2b2b;letter-spacing:1px}
.login input{position:absolute;top:97px;height:20px;border:1px solid var(--line);font-family:inherit;font-size:10.5px;padding-left:7px;color:var(--muted);background:var(--white)}
.login .user{left:587px;width:123px}
.login .pass{left:721px;width:122px}
.btn-small{position:absolute;top:96px;height:21px;color:var(--white);font-size:12px;font-weight:700;display:flex;align-items:center;justify-content:center;border-radius:2px}
.btn-signin{left:851px;width:62px;background:var(--blue)}
.btn-register{left:919px;width:73px;background:var(--red)}

/* nav */
.mainnav{position:absolute;left:200px;top:139px;width:793px;height:32px;background:linear-gradient(var(--nav-top),var(--nav-bottom));border-radius:3px;display:flex}
.mainnav a{color:var(--white);font-size:13px;display:flex;align-items:center;padding:0 17px;border-right:1px solid #1b1919;height:100%}
.mainnav a:last-child{border-right:none}

/* content */
.panel{position:absolute;left:201px;top:182px;width:792px;height:387px;border:1px solid #dcdcdc;box-shadow:0 0 3px rgba(0,0,0,.18);background:var(--white)}
.contact__title{position:absolute;left:278px;top:213px;font-size:27px;font-weight:700;color:var(--ink)}
.contact-form .field{position:absolute;left:269px;width:253px;height:25px;border:1px solid var(--line);font-family:inherit;font-size:10.5px;color:var(--muted);padding:7px 11px}
.f-name{top:266px}.f-email{top:308px}.f-mobile{top:348px}
.f-message{top:390px;height:93px !important}
.btn-submit{position:absolute;left:446px;top:492px;width:75px;height:23px;background:linear-gradient(#8cc6ea,var(--blue-dark));color:var(--white);font-size:12.5px;font-weight:700;display:flex;align-items:center;justify-content:center;border-radius:2px}
.contact-line{position:absolute;top:227px;display:flex;align-items:center;gap:10px;font-size:15.5px;color:#4a4a4a}
.contact-line--phone{left:569px}
.contact-line--mail{left:718px}
.map{position:absolute;left:571px;top:268px;width:404px;height:236px;background:linear-gradient(180deg,var(--map-sand) 0%,var(--map-warm) 45%,var(--map-river) 62%,var(--map-sand) 100%)}

/* footer */
.footer{position:absolute;left:0;top:609px;width:1200px;height:223px;background:var(--footer);color:var(--white)}
.about{position:absolute;left:200px;top:14px;width:335px}
.about h2{font-size:17px;font-weight:700;margin-bottom:10px}
.about p{font-size:10.6px;line-height:13.2px}
.social{position:absolute;left:199px;top:135px;display:flex;gap:9px}
.social span{width:21px;height:21px;background:#b9b6b6;border-radius:2px}
.fcol{position:absolute;top:23px}
.fcol h3{font-size:14px;font-weight:700;margin-bottom:9px}
.fcol li{list-style:none;font-size:11px;line-height:18.6px}
.fcol--employers{left:588px}.fcol--grooms{left:700px}.fcol--jobs{left:803px}
.footer__rule{position:absolute;left:0;top:177px;width:1200px;height:1px;background:#595556}
.copyright{position:absolute;left:285px;top:194px;font-size:11px}
.copyright a{color:var(--link)}
</style>
</head>
<body>
<div class="page">
  <div class="topbar">
    <a class="tab tab--seekers" href="#">Job seekers</a>
    <a class="tab tab--employers" href="#">Employers</a>
    <span class="topbar__prompt">Looking to Post a job?</span>
    <a class="btn-post" href="#">Click here</a>
  </div>

  <header>
    <div class="brand"><span class="brand__mark"></span><span class="brand__name">Stablemark Hire</span></div>
    <form class="login">
      <input class="user" type="text" placeholder="User name">
      <input class="pass" type="password" placeholder="Password">
    </form>
    <a class="btn-small btn-signin" href="#">Sign in</a>
    <a class="btn-small btn-register" href="#">Register</a>
  </header>

  <nav class="mainnav">
    <a href="#">Home</a><a href="#">About US</a><a href="#">Employers</a><a href="#">Advertise</a><a href="#">News</a><a href="#">Resources</a><a href="#">Helpful links</a>
  </nav>

  <main class="panel"></main>
  <h1 class="contact__title">Contact Us</h1>
  <form class="contact-form">
    <div class="field f-name">Your name</div>
    <div class="field f-email">email address</div>
    <div class="field f-mobile">Mobile number</div>
    <div class="field f-message">Your Message</div>
    <a class="btn-submit" href="#">Submit</a>
  </form>

  <div class="contact-line contact-line--phone">
    <svg width="22" height="19" viewBox="0 0 22 19"><path d="M2 5c0-3 18-3 18 0v2h-5V5H7v2H2z" fill="#3a3a3a"/><rect x="4" y="8" width="14" height="10" rx="1" fill="#3a3a3a"/><circle cx="11" cy="13" r="3" fill="#fff"/></svg>
    <span>08450117392</span>
  </div>
  <div class="contact-line contact-line--mail">
    <svg width="21" height="14" viewBox="0 0 21 14"><rect width="21" height="14" rx="1" fill="#3a3a3a"/><path d="M1 1l9.5 7L20 1" stroke="#fff" stroke-width="1.6" fill="none"/></svg>
    <span>info@stablemarkhire.co.uk</span>
  </div>

  <div class="map" role="img" aria-label="Street map with a marker showing the office location"></div>

  <footer class="footer">
    <div class="about">
      <h2>About Stablemark Hire</h2>
      <p>Lorem Ipsum is simply dummy text of the printing and typesetting industry. Lorem Ipsum has been the industry's standard dummy text ever since the 1500s, when an unknown printer took a galley of type and scrambled it to make a type specimen book. It has survived not only five centuries, but also the leap into electronic typesetting, remaining essentially unchanged.</p>
    </div>
    <div class="social"><span></span><span></span><span></span><span></span></div>
    <div class="fcol fcol--employers"><h3>Employers</h3><ul><li>What you get</li><li>How we work</li><li>Register</li><li>Login</li><li>Groom Search</li><li>FAQs</li></ul></div>
    <div class="fcol fcol--grooms"><h3>Grooms</h3><ul><li>What you get</li><li>How we work</li><li>Register CV</li><li>Login</li><li>Job Search</li><li>FAQs</li></ul></div>
    <div class="fcol fcol--jobs"><h3>Featured jobs</h3><ul><li>Head Groom</li><li>Stallion Hander - Australia</li><li>Instructor rider</li><li>Riding Instructor</li><li>Polo Groom</li><li>secretary/admin/telesales</li></ul></div>
    <div class="footer__rule"></div>
    <p class="copyright">Copyright Stablemark Hire 2012. Use of this website constitutes acceptance of our <a href="#">User Agreement and Privacy Policy</a></p>
  </footer>
</div>
</body>
</html>
```